I require a logo design and business card design.

The logo and business card is for a pre existing salon that I have purchased in the last 6 months. It is about to get a total facelift and so requires rebranding. It is currently very dated and only appeals to an older demographic, I'm hoping to keep existing clients but also encourage new and younger clients who will have more creative work done. The salon is in a seaside location, we have tourists as clients also. I would like the logo to reflect the creative nature of my business.
Target Market(s)
All ages, men and women. Middle to upper price demographic.
Industry/Entity Type
Business
Logo on the front. Logo, address and phone number on the back.
Colors
Designer to choose colors to be used in the design.
Requirements
Must have
- On the back of the card I also require 'next appointment details (date and time). As well as the salon name 'brightfern hair design', the phone number 0257318492, and address 17 Wollemby road Marlow Heads.

Nice to have
- The salon has round mirrors, that could be part of a theme. It is also located in a coastal region, so that could be part of a theme.

Should not have
- Not too busy please

```html
<!DOCTYPE html>
<html lang="en">
<head>
<meta charset="utf-8">
<title>Brightfern Hair Design – Business Card</title>
<link rel="stylesheet" href="https://fonts.googleapis.com/css2?family=Didact+Gothic&display=swap">
<style>
  :root {
    --sea-blue: #33bdf2;
    --sea-blue-deep: #2aa7d9;
    --espresso: #4a1a0c;
    --ink: #3a2a24;
    --accent-blue: #2fb3ea;
    --paper: #ffffff;
    --backdrop: #ffffff;
    --shadow: rgba(0, 0, 0, 0.45);
  }
  * { box-sizing: border-box; margin: 0; padding: 0; }
  html, body {
    width: 1015px;
    height: 1200px;
    overflow: hidden;
    background: var(--backdrop);
    font-family: "Didact Gothic", "Century Gothic", sans-serif;
  }
  .canvas {
    position: relative;
    width: 1015px;
    height: 1200px;
  }
  .card {
    position: absolute;
    left: 27px;
    width: 961px;
    height: 563px;
    box-shadow: 0 0 9px var(--shadow);
    overflow: hidden;
  }
  .card--front { top: 25px; background: var(--sea-blue); }
  .card--back { top: 615px; height: 566px; background: var(--paper); }

  .portrait-area {
    position: absolute;
    left: 79px;
    top: 19px;
    width: 320px;
    height: 531px;
    border-radius: 48% 52% 40% 45% / 38% 40% 30% 32%;
    background: radial-gradient(ellipse at 50% 40%, var(--sea-blue-deep) 0%, var(--sea-blue) 75%);
  }

  .brand-name {
    position: absolute;
    color: var(--espresso);
    line-height: 1;
  }
  .brand-name__main {
    display: block;
    font-size: 66px;
    letter-spacing: 1px;
  }
  .brand-name__sub {
    display: block;
    margin-top: 26px;
    font-size: 33px;
    letter-spacing: 10px;
    text-transform: uppercase;
  }
  .card--front .brand-name { left: 513px; top: 68px; }

  .rule {
    position: absolute;
    height: 2px;
    background: var(--espresso);
  }
  .card--front .rule { left: 490px; top: 253px; width: 351px; }

  .contact { position: absolute; left: 491px; color: var(--ink); }
  .contact--phone { top: 293px; font-size: 36px; letter-spacing: 1px; }
  .contact--address { top: 372px; font-size: 31px; line-height: 1.3; }

  .card--back .brand-name {
    left: 0;
    right: 0;
    top: 52px;
    text-align: center;
  }
  .card--back .brand-name__sub { padding-left: 10px; }
  .card--back .rule { left: 309px; top: 232px; width: 346px; }

  .appointment-heading {
    position: absolute;
    left: 0;
    right: 0;
    top: 283px;
    text-align: center;
    color: var(--accent-blue);
    font-size: 33px;
    font-style: italic;
  }
  .appointment-field {
    position: absolute;
    top: 432px;
    display: flex;
    align-items: baseline;
    color: var(--ink);
    font-size: 30px;
  }
  .appointment-field--date { left: 70px; }
  .appointment-field--time { left: 602px; }
  .write-line {
    display: inline-block;
    margin-left: 8px;
    border-bottom: 2px solid var(--ink);
    transform: translateY(2px);
  }
  .appointment-field--date .write-line { width: 390px; }
  .appointment-field--time .write-line { width: 205px; }
</style>
</head>
<body>
<main class="canvas">
  <section class="card card--front">
    <div class="portrait-area" role="img" aria-label="Line illustration of a woman with long flowing hair"></div>
    <div class="brand-name">
      <span class="brand-name__main">Brightfern</span>
      <span class="brand-name__sub">Hair Design</span>
    </div>
    <div class="rule"></div>
    <p class="contact contact--phone">02 5731 8492</p>
    <p class="contact contact--address">17 Wollemby Road<br>Marlow Heads</p>
  </section>

  <section class="card card--back">
    <div class="brand-name">
      <span class="brand-name__main">Brightfern</span>
      <span class="brand-name__sub">Hair Design</span>
    </div>
    <div class="rule"></div>
    <p class="appointment-heading">Your next appointment is:</p>
    <p class="appointment-field appointment-field--date">DATE:<span class="write-line"></span></p>
    <p class="appointment-field appointment-field--time">TIME:<span class="write-line"></span></p>
  </section>
</main>
</body>
</html>
```